Website redesign

We need a bold revamp of our website (http://www.brantocksparkworks.co.nz/)
which at the moment looks dated. We want a crisp, fresh and bold look. The background image behind web page can go. Open to complete new layout

Target Market(s)

Electrical contracting company- working in the domestic and commercial field

Coding

Coded - Design and coding required

Number of Pages Required

5+ page

Font styles to use
Sans Serif

Colors

Designer to choose colors to be used in the design.

```html
<!DOCTYPE html>
<html lang="en">
<head>
<meta charset="utf-8">
<title>Brantock Sparkworks — Home</title>
<link rel="stylesheet" href="https://fonts.googleapis.com/css2?family=Open+Sans:wght@400;600&family=Roboto:wght@300;400;700&display=swap">
<style>
  :root {
    --red: #e8160c;
    --red-glass: rgba(196, 22, 34, 0.72);
    --ink: #2b2f4a;
    --muted: #8a8fae;
    --body: #7a7d8c;
    --white: #ffffff;
    --page: #ffffff;
    --brand-ink: #151515;
    --warehouse-a: #c9ced3;
    --warehouse-b: #56606a;
    --night-a: #2c3a72;
    --night-b: #35343a;
  }
  * { box-sizing: border-box; margin: 0; padding: 0; }
  html, body { width: 1200px; height: 676px; overflow: hidden; background: var(--page); }
  body { font-family: "Open Sans", Arial, sans-serif; position: relative; }

  .site-header { position: absolute; top: 0; left: 0; width: 1200px; height: 110px; background: var(--white); }
  .contact-strip {
    position: absolute; top: 0; right: 0; width: 790px; height: 36px;
    background: var(--red);
    clip-path: polygon(0 0, 100% 0, 100% 100%, 38px 100%);
    display: flex; justify-content: flex-end; align-items: center; gap: 30px;
    padding-right: 46px; color: var(--white); font-size: 11px; font-weight: 600;
  }
  .contact-strip span { display: flex; align-items: center; gap: 5px; }
  .contact-strip svg { width: 11px; height: 11px; fill: var(--white); }

  .brand { position: absolute; left: 50px; top: 30px; display: flex; align-items: center; gap: 10px; text-decoration: none; }
  .brand-mark { width: 22px; height: 22px; background: var(--red); }
  .brand-name { font-family: "Roboto", Arial, sans-serif; font-weight: 700; font-size: 24px; color: var(--brand-ink); line-height: 1.05; }

  .main-nav { position: absolute; top: 62px; right: 48px; display: flex; gap: 38px; }
  .main-nav a { font-size: 12.5px; color: var(--ink); text-decoration: none; letter-spacing: 0.2px; }
  .main-nav a.is-current { color: var(--red); }

  .hero { position: absolute; top: 110px; left: 0; width: 1200px; height: 450px; overflow: hidden; }
  .hero-commercial { position: absolute; inset: 0; background: linear-gradient(170deg, var(--warehouse-b) 0%, #8a939b 40%, var(--warehouse-a) 75%, #e2e5e8 100%); }
  .hero-domestic {
    position: absolute; inset: 0;
    background: linear-gradient(165deg, var(--night-a) 0%, #3a4170 50%, var(--night-b) 100%);
    clip-path: polygon(740px 0, 1200px 0, 1200px 450px, 520px 450px);
  }
  .hero-badge {
    position: absolute; left: 478px; top: 98px; width: 250px; height: 250px; border-radius: 50%;
    background: var(--red-glass);
    display: flex; flex-direction: column; align-items: center; justify-content: center;
    font-family: "Roboto", Arial, sans-serif; color: var(--white); text-align: center; line-height: 1.12;
  }
  .hero-badge .light { font-weight: 300; font-size: 30px; letter-spacing: 1px; }
  .hero-badge .strong { font-weight: 700; font-size: 38px; }

  .about { position: absolute; top: 560px; left: 0; width: 1200px; height: 116px; }
  .about-kicker { position: absolute; left: 92px; top: 22px; font-size: 14px; color: var(--muted); }
  .about-title { position: absolute; left: 94px; top: 40px; font-size: 27px; font-weight: 400; color: var(--ink); }
  .about-text { position: absolute; left: 96px; top: 82px; width: 540px; font-size: 11.5px; line-height: 16px; color: var(--body); }
  .about-photo {
    position: absolute; left: 720px; top: 52px; width: 380px; height: 70px;
    background: linear-gradient(90deg, #d9d9db 0%, #eeeeef 55%, #c9a98a 90%, #e8e8e8 100%);
    box-shadow: 0 0 16px rgba(232, 22, 12, 0.18);
  }
</style>
</head>
<body>
  <header class="site-header">
    <div class="contact-strip">
      <span><svg viewBox="0 0 24 24"><path d="M6.6 10.8a15.1 15.1 0 0 0 6.6 6.6l2.2-2.2a1 1 0 0 1 1-.25 11.4 11.4 0 0 0 3.6.57 1 1 0 0 1 1 1V20a1 1 0 0 1-1 1A17 17 0 0 1 3 4a1 1 0 0 1 1-1h3.5a1 1 0 0 1 1 1c0 1.25.2 2.45.57 3.57a1 1 0 0 1-.25 1z"/></svg>+1 800 555 01 47</span>
      <span><svg viewBox="0 0 24 24"><path d="M2 5h20v14H2z M2 5l10 8 10-8" /></svg>info@brantocksparkworks.co.nz</span>
    </div>
    <a class="brand" href="#">
      <span class="brand-mark"></span>
      <span class="brand-name">Brantock<br>Sparkworks</span>
    </a>
    <nav class="main-nav">
      <a class="is-current" href="#">HOME</a>
      <a href="#">ABOUT US</a>
      <a href="#">OUR SERVICES</a>
      <a href="#">PROJECTS</a>
      <a href="#">BLOG</a>
      <a href="#">CONTACT US</a>
    </nav>
  </header>

  <section class="hero">
    <div class="hero-commercial" role="img" aria-label="Photo of a large empty warehouse lit by rows of ceiling lights"></div>
    <div class="hero-domestic" role="img" aria-label="Photo of a modern glass-fronted house lit up at dusk"></div>
    <div class="hero-badge">
      <span class="light">DO YOU</span>
      <span class="strong">NEED</span>
      <span class="light">A</span>
      <span class="light">ELECTRICIAN</span>
    </div>
  </section>

  <section class="about">
    <p class="about-kicker">About Us</p>
    <h2 class="about-title">Who we are ?</h2>
    <p class="about-text">We have many years of foreign experience on projects for affluent clients.<br>We know, how to privde high quality work, While on the job site, We do not perceive</p>
    <div class="about-photo" role="img" aria-label="Portrait photo of a team member in a bright room"></div>
  </section>
</body>
</html>
```